Business Card Design (NEW FILES)

ATTENTION: New vector files are available. Please update your design to reflect/use the new (better resolution) logo images.

Seeking a unique and professional business card design for a commercial drone photography/videography business. The layout should feature
the logo (attached) and include the following information:
978-512-6037
www.skyvantmedia.com
ORD Certified Remote Pilot

```html
<!DOCTYPE html>
<html lang="en">
<head>
<meta charset="utf-8">
<title>Skyvant Media Business Card</title>
<link href="https://fonts.googleapis.com/css2?family=Arimo:ital,wght@0,400;0,700;1,400&display=swap" rel="stylesheet">
<style>
  :root {
    --navy: #12163f;
    --orange: #ec8445;
    --white: #ffffff;
    --backdrop: #1b1b1d;
  }
  * { box-sizing: border-box; margin: 0; padding: 0; }
  html, body {
    width: 1200px; height: 963px; overflow: hidden;
    background: var(--backdrop);
    font-family: "Arimo", Arial, sans-serif;
  }
  .canvas {
    width: 1200px; height: 963px;
    display: flex; flex-direction: column; align-items: center; justify-content: center;
    gap: 40px;
  }
  .card {
    position: relative;
    width: 700px; height: 400px;
    border-radius: 28px;
    overflow: hidden;
  }
  .card--front { background: var(--white); color: var(--navy); }
  .card--back { background: var(--navy); color: var(--white); }

  .brand {
    position: absolute; left: 44px; top: 56px;
    display: flex; align-items: center; gap: 18px;
  }
  .brand__dot {
    width: 96px; height: 96px; border-radius: 50%;
    border: 13px solid var(--navy);
    flex: none;
  }
  .brand__name {
    font-size: 30px; font-weight: 700; letter-spacing: 1px; color: var(--navy);
    white-space: nowrap;
  }

  .person {
    position: absolute; right: 68px; top: 196px; text-align: right;
  }
  .person__name {
    font-size: 25px; font-weight: 700; letter-spacing: 1px; text-transform: uppercase;
    white-space: nowrap;
  }
  .person__name .surname { color: var(--orange); }
  .person__role { font-size: 17px; margin-top: 4px; }
  .accent-bar {
    position: absolute; right: 0; top: 216px;
    width: 36px; height: 44px; background: var(--orange);
  }

  .contact {
    position: absolute; left: 150px; top: 250px;
    font-size: 18px; line-height: 1.5;
  }
  .contact__row { display: flex; align-items: center; gap: 10px; }
  .contact__icon { width: 16px; height: 16px; flex: none; }

  .back-brand {
    position: absolute; inset: 0;
    display: flex; flex-direction: column; align-items: center; justify-content: center; gap: 14px;
  }
  .back-brand__name { font-size: 52px; font-weight: 400; letter-spacing: 3px; text-transform: uppercase; }
  .back-brand__tagline {
    font-size: 18px; letter-spacing: 2px; text-transform: uppercase; color: var(--orange);
  }
</style>
</head>
<body>
<main class="canvas">
  <section class="card card--front">
    <div class="brand">
      <span class="brand__dot"></span>
      <span class="brand__name">Skyvant Media</span>
    </div>

    <div class="person">
      <p class="person__name">Mark <span class="surname">Doyle</span></p>
      <p class="person__role">Owner</p>
    </div>
    <span class="accent-bar"></span>

    <div class="contact">
      <p class="contact__row">
        <svg class="contact__icon" viewBox="0 0 24 24" aria-hidden="true">
          <path fill="#ec8445" d="M6.6 10.8c1.4 2.8 3.8 5.1 6.6 6.6l2.2-2.2c.3-.3.7-.4 1-.2 1.1.4 2.3.6 3.6.6.6 0 1 .4 1 1V20c0 .6-.4 1-1 1C10.6 21 3 13.4 3 4c0-.6.4-1 1-1h3.5c.6 0 1 .4 1 1 0 1.3.2 2.5.6 3.6.1.3 0 .7-.2 1l-2.3 2.2z"/>
        </svg>
        978-512-6037
      </p>
      <p class="contact__row">
        <svg class="contact__icon" viewBox="0 0 24 24" aria-hidden="true">
          <g fill="none" stroke="#ec8445" stroke-width="2">
            <circle cx="12" cy="12" r="9"/>
            <path d="M3 12h18M12 3c3 3 3 15 0 18M12 3c-3 3-3 15 0 18"/>
          </g>
        </svg>
        www.skyvantmedia.com
      </p>
      <p>ORD Certified Remote Pilot</p>
      <p>Fully Insured</p>
    </div>
  </section>

  <section class="card card--back">
    <div class="back-brand">
      <p class="back-brand__name">Skyvant Media</p>
      <p class="back-brand__tagline">Captivating Aerial Imagery</p>
    </div>
  </section>
</main>
</body>
</html>
```